Whitmore Business Card Design

The name of the business is Dara Whitmore, CPA LLC
The service that we offer is Accounting, Tax & Consulting Services. I need it to have the following items:
Dara Whitmore, Principal
Phone Number
Email Address
Physical Address

I have attached the company logo, one in black and one in white. Please provide a design in black background and the other in white background. Please include "Accounting, Tax & Consulting Services". I want the business card to be clean and very professional.

```html
<!DOCTYPE html>
<html lang="en">
<head>
<meta charset="utf-8">
<title>Dara Whitmore, CPA LLC — Business Cards</title>
<link href="https://fonts.googleapis.com/css2?family=Montserrat:wght@400;500;600&display=swap" rel="stylesheet">
<style>
  :root {
    --backdrop: #ececec;
    --card-light: #ffffff;
    --card-dark: #050606;
    --ink: #3a3a3a;
    --ink-soft: #444444;
    --grey: #8a8a8a;
    --grey-dark: #5a5a5a;
    --accent: #9e1f24;
  }
  * { margin: 0; padding: 0; box-sizing: border-box; }
  html, body {
    width: 1200px; height: 1200px; overflow: hidden;
    background: var(--backdrop);
    font-family: "Montserrat", Arial, sans-serif;
  }
  .card {
    position: absolute; left: 148px; width: 904px; height: 529px;
  }
  .card--front { top: 34px; background: var(--card-light); }
  .card--back { top: 617px; background: var(--card-dark); }

  .holder-name {
    position: absolute; left: 67px; top: 84px;
    font-size: 28px; font-weight: 600; color: var(--ink); letter-spacing: 0.01em;
  }
  .holder-role {
    position: absolute; left: 69px; top: 127px;
    font-size: 17px; font-weight: 600; color: var(--ink-soft); letter-spacing: 0.08em;
  }
  .address {
    position: absolute; left: 69px; top: 218px;
    font-size: 18px; line-height: 30px; color: var(--ink-soft);
  }
  .contact {
    position: absolute; left: 69px; top: 301px; list-style: none;
    font-size: 18px; line-height: 30px; color: var(--ink);
  }
  .contact li { display: flex; align-items: center; gap: 12px; }
  .contact svg { width: 17px; height: 14px; fill: var(--accent); }

  .brand { position: absolute; text-align: center; }
  .brand__mark { display: block; margin: 0 auto; background: var(--accent); }
  .brand__name { font-weight: 500; white-space: nowrap; }
  .brand__tagline { font-weight: 600; white-space: nowrap; letter-spacing: 0.04em; }

  .card--front .brand { left: 520px; width: 320px; top: 218px; }
  .card--front .brand__mark { width: 44px; height: 44px; margin-bottom: 36px; }
  .card--front .brand__name { font-size: 21px; color: var(--ink); }
  .card--front .brand__tagline { font-size: 15px; color: var(--grey); margin-top: 2px; }

  .card--back .brand { left: 152px; width: 600px; top: 128px; }
  .card--back .brand__mark { width: 64px; height: 64px; margin-bottom: 58px; }
  .card--back .brand__name { font-size: 32px; color: var(--grey-dark); }
  .card--back .brand__tagline { font-size: 23px; color: var(--grey-dark); margin-top: 4px; }

  .services {
    position: absolute; left: 0; width: 100%; top: 430px; text-align: center;
    font-size: 22px; font-weight: 500; letter-spacing: 0.27em; color: var(--grey);
  }
  .card--back .services { color: var(--grey-dark); }
</style>
</head>
<body>
  <section class="card card--front">
    <h1 class="holder-name">DARA WHITMORE</h1>
    <p class="holder-role">PRINCIPAL</p>
    <address class="address">1450 Cedar Ridge Lane NW<br>Santa Fe, NM 87505</address>
    <ul class="contact">
      <li><svg viewBox="0 0 17 14" aria-hidden="true"><path d="M2 3c2-3 11-3 13 0l-1 2-3-1V3H6v1L3 5zM4 7l2-2h5l2 2v6H4zm4.5 1a2 2 0 100 4 2 2 0 000-4z"/></svg>+1 505 555 0182</li>
      <li><svg viewBox="0 0 17 14" aria-hidden="true"><path d="M1 2h15v1L8.5 8 1 3zm0 3l7.5 5L16 5v7H1z"/></svg>dara@whitmorecpa.com</li>
    </ul>
    <div class="brand">
      <span class="brand__mark"></span>
      <p class="brand__name">DARA WHITMORE, CPA LLC</p>
      <p class="brand__tagline">CERTIFIED PUBLIC ACCOUNTANT</p>
    </div>
    <p class="services">ACCOUNTING, TAX &amp; CONSULTING SERVICES</p>
  </section>

  <section class="card card--back">
    <div class="brand">
      <span class="brand__mark"></span>
      <p class="brand__name">DARA WHITMORE, CPA LLC</p>
      <p class="brand__tagline">CERTIFIED PUBLIC ACCOUNTANT</p>
    </div>
    <p class="services">ACCOUNTING, TAX &amp; CONSULTING SERVICES</p>
  </section>
</body>
</html>
```